Need a fun and informative infographic!

We need an infographic to describe our "client experience" which consists of 4 phases - see info about each of our "phases" which includes our available suite of services. UPDATED THE TEXT IN A NEW FILE CALLED "Client Experience Infographic Info".

We intend to use the infographic in both print and digital in a printed "leave behind", in packets for new clients, and possible on the website.

Lantern Tutors www.lanterntutors.example

Target Market(s)

Families of children aged Kindergarten through 12th Grade; affluent communities who have expendable income to spend on private tutoring and test prep.

Industry/Entity Type

Education

Font styles to use
Sans Serif

Requirements
Must have
• My project must use our brand colors.
• Light Blue CMYK: 60 27 0 0 RGB: 115 165 215
• Dark Blue CMYK: 93 85 36 27 RGB: 43 57 94
• Orange CMYK: 0 46 77 10 RGB: 230 125 53

```html
<!DOCTYPE html>
<html lang="en">
<head>
<meta charset="utf-8">
<title>The Client Experience – Lantern Tutors</title>
<link rel="stylesheet" href="https://fonts.googleapis.com/css2?family=Arimo:wght@400;700&display=swap">
<style>
  :root {
    --orange: #e67d35;
    --orange-deep: #c9672a;
    --blue-light: #73a5d7;
    --blue-light-deep: #5b8dc0;
    --blue-dark: #2b395e;
    --ink: #1f2b4d;
    --white: #ffffff;
    --bg-top: #f4f5f6;
    --bg-bottom: #d3d6da;
  }
  * { box-sizing: border-box; margin: 0; padding: 0; }
  html, body { width: 928px; height: 1200px; overflow: hidden; }
  body {
    font-family: "Arimo", Arial, sans-serif;
    background: radial-gradient(ellipse 70% 60% at 50% 30%, var(--bg-top), var(--bg-bottom));
    position: relative;
  }
  .brand { position: absolute; left: 28px; top: 56px; width: 150px; text-align: center; }
  .brand-mark {
    display: block; margin: 0 auto 10px;
    width: 100px; height: 100px; border-radius: 50%;
    background: var(--blue-light); border: 8px solid var(--white);
    box-shadow: 0 0 0 4px var(--blue-light-deep);
  }
  .brand-name { color: var(--blue-dark); font-weight: 700; font-size: 17px; }

  .title-frame {
    position: absolute; left: 190px; top: 76px; width: 697px; height: 83px;
    background: linear-gradient(#ffffff, #e4e6e9);
    border: 2px solid #c8ccd1; border-radius: 4px;
    box-shadow: 0 3px 8px rgba(0,0,0,.25);
    padding: 16px 14px 0 18px;
  }
  .title-bar {
    height: 56px; background: var(--blue-dark);
    display: flex; align-items: center; justify-content: center;
    box-shadow: inset 0 0 0 2px #22304f;
  }
  .title-bar h1 { color: var(--white); font-size: 37px; font-weight: 700; letter-spacing: .3px; }

  .phase { position: absolute; top: 273px; width: 179px; }
  .phase:nth-of-type(1) { left: 38px; }
  .phase:nth-of-type(2) { left: 268px; }
  .phase:nth-of-type(3) { left: 496px; }
  .phase:nth-of-type(4) { left: 720px; }
  .phase.orange { --c: var(--orange); --cd: var(--orange-deep); }
  .phase.blue { --c: var(--blue-light); --cd: var(--blue-light-deep); }

  .phase-head {
    height: 124px; background: var(--c);
    border-left: 5px solid var(--cd);
    color: var(--white); text-align: center; padding-top: 10px;
  }
  .phase-word { display: block; font-size: 38px; line-height: 44px; }
  .phase-num { display: block; font-size: 50px; font-weight: 700; line-height: 54px; }

  .phase-label {
    margin: 0 12px; height: 108px; background: var(--white);
    box-shadow: 0 4px 6px rgba(0,0,0,.2);
    display: flex; align-items: flex-start; justify-content: center;
    padding-top: 30px; text-align: center;
    color: var(--ink); font-weight: 700; font-size: 16px; line-height: 20px;
  }
  .phase-body {
    margin-top: 3px; height: 500px; background: var(--c);
    border-left: 5px solid var(--cd);
    color: var(--white); font-size: 13.4px; line-height: 16px;
    padding: 0 8px 0 14px;
    display: flex; flex-direction: column; justify-content: center;
  }
  .phase.first .phase-body { padding-bottom: 60px; }
  .phase.last .phase-body { justify-content: flex-start; padding-top: 8px; }
  .phase-body ul { list-style: none; }
  .phase-body li { padding-left: 0; }
  .phase-body li::before { content: "•\00a0\00a0\00a0\00a0"; }
  .phase-body li.sub::before { content: "o\00a0\00a0\00a0\00a0"; }
  .reflection {
    height: 82px;
    background: linear-gradient(to bottom, var(--c), rgba(255,255,255,0));
    opacity: .35;
  }
</style>
</head>
<body>
  <div class="brand">
    <span class="brand-mark"></span>
    <span class="brand-name">Lantern Tutors</span>
  </div>

  <header class="title-frame">
    <div class="title-bar"><h1>The Client Experience</h1></div>
  </header>

  <section class="phase orange first">
    <div class="phase-head"><span class="phase-word">Phase</span><span class="phase-num">01</span></div>
    <div class="phase-label">The<br>Consultation</div>
    <div class="phase-body">
      <ul>
        <li>The process begins with a complimentary and thorough consultation.</li>
        <li>One of our local Educational Directors meets in-person (or via VidLink if necessary ) with the parents and student to become acquainted and to better understand the family's needs.</li>
      </ul>
    </div>
    <div class="reflection"></div>
  </section>

  <section class="phase blue">
    <div class="phase-head"><span class="phase-word">Phase</span><span class="phase-num">02</span></div>
    <div class="phase-label">Match and<br>Customize</div>
    <div class="phase-body">
      <ul>
        <li>Students are matched with a tutor or a team of tutors based on a careful understanding of each student's unique learning style, academic goals, personality, and schedule.</li>
        <li>The tutor(s) develop a personalized curriculum that aligns with the student's existing strengths and areas for improvement, while addressing all factors impacting performance such as test anxiety and self-confidence.</li>
      </ul>
    </div>
    <div class="reflection"></div>
  </section>

  <section class="phase orange">
    <div class="phase-head"><span class="phase-word">Phase</span><span class="phase-num">03</span></div>
    <div class="phase-label">Communication</div>
    <div class="phase-body">
      <ul>
        <li>Tutoring sessions occur in the home, our offices, remotely or a location of the family's choosing; scheduling is based on the availability of the student.</li>
        <li>Our custom-built, mobile-friendly "Dashboard" provides parents with a thorough lesson summary after each session, convenient practice test registration, and real-time tracking of student progress.</li>
      </ul>
    </div>
    <div class="reflection"></div>
  </section>

  <section class="phase blue last">
    <div class="phase-head"><span class="phase-word">Phase</span><span class="phase-num">04</span></div>
    <div class="phase-label">Ongoing Suite<br>of Services</div>
    <div class="phase-body">
      <ul>
        <li>Our Educational Directors are compassionate and responsive, ready to provide guidance and seamless coordination of whatever services the student requires.</li>
        <li>No matter where along the path our relationship begins, we continue to support our students and families in a myriad of ways including:</li>
        <li class="sub">Standardized Test Prep</li>
        <li class="sub">Subject Tutoring</li>
        <li class="sub">College Admissions Consulting</li>
        <li>When appropriate, we introduce behaviors for students to improve their executive functioning, organizational and time management.</li>
      </ul>
    </div>
    <div class="reflection"></div>
  </section>
</body>
</html>
```